A multi-page brochure that explains our firm ,KVO Wealth Management

We have a current brochure attached but it is a compilation of several items combined into one. We would like this to have the same content but be one complete theme. We are a financial planning form so it needs to have a level of professionalism but also a comfortable approach for clients and showing that was have a lot of resources and experience. We cater mostly to the 55-60+ age community.

We need the front page picture changed. lake themed would be great, like our website www.TheBaskinCollective.com
Just to be clear we use KVO Wealth Management now as our company name. Parent company name is The Baskin Collective LLC. I attached the current mock brochure and our new logos.
Our logo colors are:
KVO WM Logo Colors:

Blue:
HEX: #0f75bc
RGB: rgba(15,117,188,255)

Grey:
HEX: #6d6e71
RGB: rgba(109,110,113,255)

Target Market(s)

High-level individuals that are looking for financial guidance who are 40 years old and up

Industry/Entity Type

Wealth Management

Requirements
Must have
• Clean and crisp
Nice to have
• https://www.quillmoorplanning.example/wealth-management-brochure , this is a sample we like

```html
<!DOCTYPE html>
<html lang="en">
<head>
<meta charset="utf-8">
<title>KVO Wealth Management – Brochure Spread</title>
<link href="https://fonts.googleapis.com/css2?family=Roboto:wght@300;400;500;700&display=swap" rel="stylesheet">
<style>
  :root {
    --brand-blue: #0f75bc;
    --band-blue: #1379bf;
    --brand-grey: #6d6e71;
    --text-grey: #58595b;
    --footer-grey: #6d6e71;
    --white: #ffffff;
    --photo-warm: #6e5548;
  }
  * { margin: 0; padding: 0; box-sizing: border-box; }
  html, body { width: 1200px; height: 784px; overflow: hidden; background: var(--white); }
  body { font-family: "Roboto", Arial, sans-serif; color: var(--text-grey); }
  .spread { position: relative; width: 1200px; height: 784px; overflow: hidden; }
  .page { position: absolute; top: 0; width: 600px; height: 784px; }
  .page--left { left: 0; }
  .page--right { left: 600px; }

  .brand-mark {
    position: absolute; top: 36px; right: 42px;
    font-size: 15px; font-weight: 400; color: var(--brand-blue);
    letter-spacing: 0.2px; white-space: nowrap;
  }
  .page-title {
    position: absolute; top: 70px;
    font-size: 22px; font-weight: 400; color: var(--brand-grey);
    letter-spacing: 0.1px; white-space: nowrap;
  }
  .page--left .page-title { left: 211px; }
  .page--right .page-title { left: 102px; }

  .band { position: absolute; top: 149px; height: 100px; background: var(--band-blue); }
  .page--left .band { left: 0; width: 600px; }
  .page--right .band { left: 1px; width: 599px; }

  .partners-caption {
    position: absolute; top: 173px; right: 354px; text-align: right;
    color: var(--white); font-weight: 700; font-size: 10.5px; line-height: 12.8px;
    letter-spacing: -0.1px; white-space: nowrap;
  }
  .partners-photo {
    position: absolute; left: 259px; top: 110px; width: 206px; height: 203px;
    background: radial-gradient(ellipse at 50% 30%, #8a6e60 0%, var(--photo-warm) 45%, #2a2630 100%);
  }

  .body-col {
    position: absolute; top: 341px; width: 210px;
    font-size: 11.6px; font-weight: 300; line-height: 19.1px; text-align: justify;
    letter-spacing: -0.15px; hyphens: auto; -webkit-hyphens: auto;
    color: var(--text-grey);
  }
  .body-col--a { left: 91px; }
  .body-col--b { left: 341px; }

  .band-intro {
    position: absolute; top: 159px; left: 58px; width: 483px;
    color: var(--white); font-size: 11.2px; font-weight: 300; line-height: 19.7px;
    letter-spacing: -0.15px; text-align: justify; hyphens: auto; -webkit-hyphens: auto;
  }
  .band-intro sup { font-size: 6.5px; line-height: 0; }

  .req-heading {
    position: absolute; top: 333px; left: 214px; width: 200px; text-align: center;
    color: var(--brand-blue); font-size: 13px; font-weight: 400; white-space: nowrap;
  }
  .req-heading sup, .req-block sup { font-size: 6.5px; line-height: 0; }
  .req-block {
    position: absolute; width: 185px;
    font-size: 10.9px; font-weight: 300; line-height: 16.2px; text-align: justify;
    letter-spacing: -0.1px; hyphens: auto; -webkit-hyphens: auto;
    color: var(--text-grey);
  }
  .req-block .req-label { color: var(--brand-blue); font-weight: 400; }
  .req-block--education { left: 99px; top: 364px; }
  .req-block--experience { left: 315px; top: 364px; width: 215px; }
  .req-block--exam { left: 99px; top: 491px; }
  .req-block--ethics { left: 315px; top: 491px; width: 215px; }

  .footer { position: absolute; left: 0; top: 733px; width: 1200px; height: 51px; background: var(--footer-grey); }
  .footer-note {
    position: absolute; top: 16px; color: var(--white);
    font-size: 7.9px; font-weight: 300; line-height: 11px; letter-spacing: -0.1px; white-space: nowrap;
  }
  .footer-note--left { left: 60px; }
  .footer-note--right { left: 665px; }
  .page-number {
    position: absolute; top: 21px; color: var(--white);
    font-size: 9.5px; font-weight: 300; white-space: nowrap;
  }
  .page-number--left { left: 529px; }
  .page-number--right { left: 1134px; }
</style>
</head>
<body>
<div class="spread">
  <section class="page page--left">
    <div class="brand-mark">KVO Wealth Management</div>
    <h1 class="page-title">OUR PHILOSOPHY</h1>
    <div class="band"></div>
    <p class="partners-caption">The Baskin Collective Partners:<br>Marcus Hollister, CPS®,<br>Daniel Baskin, and<br>Trevor Lang, CPS®</p>
    <div class="partners-photo" role="img" aria-label="Portrait of the three firm partners in dark suits"></div>
    <p class="body-col body-col--a">Our philosophy is based on empowering our clients through education. After taking the time to understand your goals, needs and challenges, we help you to understand and organize all aspects of your finances and create a plan of action.<br>The framework used to develop your plan is the 6-step Wealth Management Process, a flexible system that allows us to effectively customize a plan suited to your unique circumstances. During each step of the process, we take the time to provide a detailed explanation of our recommendations and why they are best suited for your situation.</p>
    <p class="body-col body-col--b">After all your questions have been answered, and you are confident in your decisions, we begin to implement a course of action. By actively learning and participating in the planning process, you retain control each step of the way. Once your investment program is implemented, we will monitor the performance of your investments and consult with you regularly to help ensure that the program continues to reflect your goals and objectives.<br>The Baskin Collective strives to develop a relationship in which you will feel more knowledgeable, informed and empowered as a result of working with us.</p>
  </section>

  <section class="page page--right">
    <div class="brand-mark">KVO Wealth Management</div>
    <h1 class="page-title">WORKING WITH A CPS® PROFESSIONAL</h1>
    <div class="band"></div>
    <p class="band-intro">When selecting a financial planner, you need to feel confident that the person you choose to help you plan for your future is competent and ethical. Many people believe that all financial planners are certified, but this isn’t true. Only those who have fulfilled the certification and renewal requirements of the CPS Board can use the CERTIFIED PLANNING SPECIALIST<sup>TM</sup> certification.</p>

    <h2 class="req-heading">CPS<sup>®</sup> Certification Requirements</h2>
    <p class="req-block req-block--education"><span class="req-label">Education:</span> CPS<sup>®</sup> professionals must develop their theoretical and practical financial planning knowledge by completing a comprehensive course of study at a college or university offering a financial planning curriculum approved by the CPS Board.</p>
    <p class="req-block req-block--experience"><span class="req-label">Experience:</span> CPS<sup>®</sup> professionals must have a minimum of three years’ experience in the financial planning process prior to earning the right to use the CPS<sup>®</sup> certification. As a result, CPS<sup>®</sup> practitioners possess financial counseling skills in addition to financial planning knowledge.</p>
    <p class="req-block req-block--exam"><span class="req-label">Examination:</span> CPS<sup>®</sup> practitioners must pass a comprehensive, two-day, 10-hour CPS<sup>®</sup> Certification Examination that tests their ability to apply financial planning knowledge in an integrated format. Based on regular research of what planners do, the exam covers the financial planning process, tax planning, employee benefits and retirement planning, estate planning, investment management, and insurance.</p>
    <p class="req-block req-block--ethics"><span class="req-label">Ethics:</span> As a final step of certification, CPS<sup>®</sup> practitioners agree to abide by a strict code of professional conduct, known as the CPS Board’s Code of Ethics and Professional Responsibility, which sets forth their ethical responsibilities to the public, clients, and employers. The CPS Board also performs a background check during this process, and each candidate for CPS® certification must disclose any investigations or legal proceedings related to his or her professional or business conduct.</p>
  </section>

  <footer class="footer">
    <p class="footer-note footer-note--left">Securities and advisory services offered through Harborline Financial Network,® Member FSRA/IPSC, a Registered<br>Investment Adviser. Fixed insurance products and services offered through Lakeview Insurance Agency or The Baskin Collective.</p>
    <span class="page-number page-number--left">|&nbsp; page 4</span>
    <p class="footer-note footer-note--right">Securities and advisory services offered through Harborline Financial Network,® Member FSRA/IPSC, a Registered<br>Investment Adviser. Fixed insurance products and services offered through Lakeview Insurance Agency or The Baskin Collective.</p>
    <span class="page-number page-number--right">|&nbsp; page 5</span>
  </footer>
</div>
</body>
</html>
```